Fun Feminine Redesign Product Landing Page

This is our current product page
https://dovelmintery.com/product/coffee-substitute/

I like the overall feel of this but it needs to pop more. I love the pink an we are in the process of having illustrations made for the how to section.

Examples with more pop
https://www.brambleoven.com/products/chicken-bone-broth?shipping=8
https://pawtonmeal.com/products/lamb-turkey-kibble-grain-free

Target Market(s)

females 24-44

Number of Pages Required

1 page

Colors
0094D4
00A9DD
6FCCEA
C7EBF8
E9F6FB
00AB8E
00BBA5
67D7C9
C6EFE9
E9F9F6
FFC000
F8CF3A
FAE287
FDF2CF
FEFAEE
E54698
E96AAD
F1A4CE
F9D9EA
FCEFF6

Requirements
Must have
• Fresh, clean, feminine and unique

```html
<!DOCTYPE html>
<html lang="en">
<head>
<meta charset="utf-8">
<title>Dovel Mintery – Original Coffee Substitute</title>
<link rel="stylesheet" href="https://fonts.googleapis.com/css2?family=Poppins:wght@500;600&family=Questrial&display=swap">
<style>
  :root{
    --stage:#E8949C;
    --panel:#FBEBEC;
    --header:#FFFFFF;
    --rule:#D9D2D3;
    --ink:#1E1E24;
    --title:#2B2D5C;
    --star:#F5C400;
    --accent:#F4969E;
    --brand:#F8CF3A;
    --photo-a:#E7DDD3;
    --photo-b:#DDD0C4;
    --thumb-stone:#E6D9CF;
    --thumb-peach:#F7D9BC;
    --veil:rgba(232,148,156,.7);
    --dot:#8E4E7E;
  }
  *{box-sizing:border-box;margin:0;padding:0}
  html,body{width:1152px;height:1200px;overflow:hidden}
  body{background:var(--stage);position:relative;font-family:"Questrial",sans-serif;color:var(--ink)}

  /* ---------- page layout (shared by both layers) ---------- */
  .page{position:absolute;left:0;top:0;width:1028px;background:var(--panel);overflow:hidden}
  .site-header{position:absolute;left:0;top:0;width:100%;height:69px;background:var(--header);border-bottom:1.5px solid var(--rule)}
  .brand{position:absolute;left:22px;top:15px;display:flex;align-items:center;gap:4px}
  .brand__dot{width:7px;height:7px;border-radius:50%;background:var(--brand)}
  .brand__name{font-family:"Questrial",sans-serif;color:var(--brand);font-size:11px;line-height:12px;width:44px}
  .nav{position:absolute;top:28px;left:0;width:100%;font-size:11.5px}
  .nav a{position:absolute;color:var(--ink);text-decoration:none;white-space:nowrap}

  .share{position:absolute;left:-70px;top:239px;width:140px;height:140px;border-radius:50%;background:var(--accent)}
  .share__item{position:absolute;left:84px;width:10px;height:10px;border-radius:50%;background:var(--title)}

  .product-photo{position:absolute;left:84px;top:112px;width:449px;height:296px;border-radius:6px;
    background:linear-gradient(135deg,var(--photo-b) 0%,var(--photo-a) 50%,var(--photo-b) 100%);
    box-shadow:0 2px 4px rgba(0,0,0,.22)}
  .thumb{position:absolute;top:432px;width:123px;height:114px;border-radius:5px}
  .thumb--stone{background:var(--thumb-stone)}
  .thumb--peach{background:var(--thumb-peach)}

  .product-title{position:absolute;left:612px;top:102px;font-family:"Poppins",sans-serif;font-weight:600;font-size:26px;line-height:34px;color:var(--title);white-space:nowrap;letter-spacing:.2px}
  .rating{position:absolute;left:615px;top:144px}
  .copy{position:absolute;left:615px;font-size:9.8px;line-height:11.6px;width:298px}
  .copy--intro{top:176px}
  .copy--more{top:228px}
  .ingredients-label{position:absolute;left:614px;top:284px;font-size:9.6px;font-family:"Poppins",sans-serif;font-weight:500;white-space:nowrap}
  .ingredients{position:absolute;left:651px;top:310px;font-size:9.8px;line-height:11.8px;width:160px}
  .price{position:absolute;left:615px;top:378px;font-family:"Poppins",sans-serif;font-weight:600;font-size:16px;white-space:nowrap}
  .price small{font-size:9.4px;font-weight:500;margin-left:3px}

  .option{position:absolute;top:428px;width:149px;height:36px;border-radius:18px;background:#fff;
    box-shadow:0 2px 3px rgba(0,0,0,.18);font-size:12.5px;display:flex;align-items:center;justify-content:center}
  .qty{position:absolute;left:620px;top:484px;width:104px;height:54px;border-radius:27px;background:#fff;
    box-shadow:0 2px 3px rgba(0,0,0,.18);font-size:15px;display:flex;align-items:center;justify-content:center}
  .qty svg{position:absolute;right:16px;top:20px}
  .add-to-cart{position:absolute;left:750px;top:484px;width:148px;height:54px;border-radius:27px;background:var(--accent);
    box-shadow:0 2px 3px rgba(0,0,0,.18);color:#fff;font-size:16.5px;display:flex;align-items:center;justify-content:center;border:none;font-family:inherit}

  /* ---------- benefits section (visible on back layer) ---------- */
  .facts{position:absolute;left:700px;top:1335px;width:506px;height:506px;border-radius:50%;background:var(--accent)}
  .facts__heading{position:absolute;left:640px;top:1464px;width:460px;font-family:"Poppins",sans-serif;font-weight:600;font-size:44px;color:#C97A84;text-align:center}
  .facts__list{position:absolute;left:700px;top:1545px;width:289px;text-align:right;font-size:13.6px;line-height:17px;color:#fff;opacity:.55}
  .facts__list p{margin-bottom:17px}
  .benefit{position:absolute;left:81px;width:527px;background:#F7DCDF;border-radius:3px}
  .benefit__dot{position:absolute;left:29px;width:34px;height:34px;border-radius:50%;background:var(--dot)}
  .benefit__title{position:absolute;left:90px;font-family:"Poppins",sans-serif;font-weight:500;font-size:17px;color:#7C3C4C}
  .benefit__text{position:absolute;left:90px;width:420px;font-size:13.4px;line-height:15.5px;color:#7C3C4C}

  /* ---------- layers ---------- */
  .layer-back{position:absolute;left:296px;top:80px;width:560px;height:1039px;overflow:hidden;box-shadow:0 2px 4px rgba(0,0,0,.15)}
  .layer-back .page{height:1906px;transform:scale(.545);transform-origin:0 0}
  .layer-back .veil{position:absolute;inset:0;background:var(--veil)}
  .layer-front{position:absolute;left:62px;top:296px;width:1028px;height:607px;box-shadow:0 3px 6px rgba(0,0,0,.2)}
  .layer-front .page{height:607px}
</style>
</head>
<body>

<!-- back layer: full-length page, muted -->
<div class="layer-back" aria-hidden="true">
  <div class="page">
    <header class="site-header">
      <div class="brand"><span class="brand__dot"></span><span class="brand__name">Dovel Mintery</span></div>
      <nav class="nav"><a style="left:645px">Learn</a><a style="left:715px">Shop</a><a style="left:767px">About</a><a style="left:825px">Contact</a><a style="left:885px">Account Login</a></nav>
    </header>
    <div class="share"><span class="share__item" style="top:30px"></span><span class="share__item" style="top:68px"></span><span class="share__item" style="top:103px"></span></div>
    <div class="product-photo" role="img" aria-label="Product photo: cup of coffee substitute with a spoon on a beige table"></div>
    <h1 class="product-title">Original Coffee Sustitite</h1>
    <svg class="rating" width="88" height="16" viewBox="0 0 88 16"><g fill="#F5C400"><polygon id="s" points="8,0 10,5.5 16,5.8 11.3,9.5 13,15.5 8,12 3,15.5 4.7,9.5 0,5.8 6,5.5"/><use href="#s" x="18"/><use href="#s" x="36"/><use href="#s" x="54"/><use href="#s" x="72"/></g></svg>
    <p class="copy copy--intro">Lorem ipsum dolor sit amet, consectetur adipiscing elit, sed do eiusmod tempor incididunt ut labore et dolore magna aliqua. Quis ipsum suspendisse ultrices gravida. Risus commodo viverra</p>
    <p class="copy copy--more">Lorem ipsum dolor sit amet, consectetur adipiscing elit, sed do eiusmod tempor incididunt ut labore et dolore magna aliqua.</p>
    <p class="ingredients-label">Three Organic Ingredients _ no extra additives:</p>
    <p class="ingredients">Lorem ipsum dolor sit amet, con-sectetur adipiscing elit, sed do eiusmod tempor incididunt ut</p>
    <p class="price">$15.00 - $28.00 - <small>or from $12.00 - $22.40/month</small></p>

    <div class="facts"></div>
    <h2 class="facts__heading">Did you know?</h2>
    <div class="facts__list">
      <p>Chicory root's components have been found to work as antioxidants and anti-inflammatories.</p>
      <p>Carob has twice the calcium of cocoa.</p>
      <p>Dandelion contains both beta-carotene, and polyphenols which work against oxidative stress in your body.</p>
    </div>
    <div class="benefit" style="top:1527px;height:97px">
      <span class="benefit__dot" style="top:36px"></span>
      <h3 class="benefit__title" style="top:13px">Minerals Galore</h3>
      <p class="benefit__text" style="top:47px">Toast to your health because our coffee substitutes are rich with calcium, copper, magnesium, selenium, zinc, and more</p>
    </div>
    <div class="benefit" style="top:1640px;height:114px">
      <span class="benefit__dot" style="top:38px"></span>
      <h3 class="benefit__title" style="top:13px">Good for the Gut</h3>
      <p class="benefit__text" style="top:46px">Chicory, Carob, and Dandelion are naturally great prebiotics! Both Chicory and Dandelion boast inulin, a great soluble dietary fiber that helps sustain healthy gut bacteria.</p>
    </div>
  </div>
  <div class="veil"></div>
</div>

<!-- front layer: product hero -->
<div class="layer-front">
  <main class="page">
    <header class="site-header">
      <div class="brand"><span class="brand__dot"></span><span class="brand__name">Dovel Mintery</span></div>
      <nav class="nav"><a href="#" style="left:645px">Learn</a><a href="#" style="left:715px">Shop</a><a href="#" style="left:767px">About</a><a href="#" style="left:825px">Contact</a><a href="#" style="left:885px">Account Login</a></nav>
    </header>
    <div class="share" aria-label="Share">
      <span class="share__item" style="top:30px"></span>
      <span class="share__item" style="top:68px"></span>
      <span class="share__item" style="top:103px"></span>
    </div>
    <div class="product-photo" role="img" aria-label="Product photo: cup of coffee substitute with a black spoon on a beige table, seen from above"></div>
    <div class="thumb thumb--stone" style="left:92px"></div>
    <div class="thumb thumb--peach" style="left:248px"></div>
    <div class="thumb thumb--stone" style="left:403px"></div>

    <h1 class="product-title">Original Coffee Sustitite</h1>
    <svg class="rating" width="88" height="16" viewBox="0 0 88 16" aria-label="5 stars"><g fill="#F5C400"><polygon id="star" points="8,0 10,5.5 16,5.8 11.3,9.5 13,15.5 8,12 3,15.5 4.7,9.5 0,5.8 6,5.5"/><use href="#star" x="18"/><use href="#star" x="36"/><use href="#star" x="54"/><use href="#star" x="72"/></g></svg>
    <p class="copy copy--intro">Lorem ipsum dolor sit amet, consectetur adipiscing elit, sed do eiusmod tempor incididunt ut labore et dolore magna aliqua. Quis ipsum suspendisse ultrices gravida. Risus commodo viverra</p>
    <p class="copy copy--more">Lorem ipsum dolor sit amet, consectetur adipiscing elit, sed do eiusmod tempor incididunt ut labore et dolore magna aliqua.</p>
    <p class="ingredients-label">Three Organic Ingredients _ no extra additives:</p>
    <p class="ingredients">Lorem ipsum dolor sit amet, con-sectetur adipiscing elit, sed do eiusmod tempor incididunt ut</p>
    <p class="price">$15.00 - $28.00 - <small>or from $12.00 - $22.40/month</small></p>

    <div class="option" style="left:615px">4 oz (15 Servings)</div>
    <div class="option" style="left:794px">4 oz (15 Servings)</div>
    <div class="qty">1
      <svg width="7" height="14" viewBox="0 0 7 14"><polygon points="3.5,0 7,5.5 0,5.5" fill="#555"/><polygon points="0,8.5 7,8.5 3.5,14" fill="#555"/></svg>
    </div>
    <button class="add-to-cart">Add to cart</button>
  </main>
</div>

</body>
</html>
```